Supplement Rebranding Bottle Design

READ WORD DOCUMENT ATTACHED.
We want to rebrand our current health supplements (see below). We do want it to be modern, vibrant and appealing. Very upscale and elegant as it targets primarily women.
Bottle size: see pictures for bottle size, along with sample bottles that we like; we’re open to any bottle similar to the ones attached.
Current bottles: So ideally, we’d keep the core color on each bottle with a new branding/bottle design. But we're open to your suggestion.

Target Market(s)

mostly women but shouldn't be overly feminine

Requirements
Must have
• see bottle sizes attached

```html
<!DOCTYPE html>
<html lang="en">
<head>
<meta charset="utf-8">
<title>Vital Tuned – Supplement Label Range</title>
<link rel="stylesheet" href="https://fonts.googleapis.com/css2?family=Outfit:wght@600&family=Arimo:wght@700&family=Nunito:wght@800&display=swap">
<style>
  :root {
    --bg: #e9e9ea;
    --tummy: #d42027;
    --hormone: #0e9443;
    --sugar: #1175bd;
    --liver: #922a8e;
    --ink-light: #ffffff;
    --brand-ink: #123a5a;
    --brand-dot: #5cb85c;
  }
  * { margin: 0; padding: 0; box-sizing: border-box; }
  html, body { width: 1200px; height: 1200px; overflow: hidden; background: var(--bg); }
  .range {
    position: relative;
    width: 1200px;
    height: 1200px;
    background: var(--bg);
  }
  .label {
    position: absolute;
    top: 0;
    width: 152px;
    height: 960px;
    color: var(--ink-light);
  }
  .label--tummy   { left: 94px;  background: var(--tummy); }
  .label--hormone { left: 381px; background: var(--hormone); }
  .label--sugar   { left: 656px; background: var(--sugar); }
  .label--liver   { left: 938px; background: var(--liver); }

  .label__frame {
    position: absolute;
    left: 24px;
    top: 354px;
    width: 104px;
    height: 104px;
  }
  .label__name {
    position: absolute;
    left: 14px;
    right: 8px;
    top: 354px;
    height: 104px;
    display: flex;
    flex-direction: column;
    justify-content: center;
    padding-left: 12px;
    font-family: "Outfit", sans-serif;
    font-weight: 600;
    font-size: 22px;
    line-height: 0.98;
    letter-spacing: -0.2px;
  }
  .label__tagline {
    position: absolute;
    left: 6px;
    right: 6px;
    top: 480px;
    text-align: center;
    font-family: "Arimo", sans-serif;
    font-weight: 700;
    font-size: 10.5px;
    line-height: 1.2;
  }
  .label__count {
    position: absolute;
    left: 12px;
    bottom: 30px;
    display: flex;
    align-items: center;
    gap: 3px;
    font-family: "Arimo", sans-serif;
    font-weight: 700;
  }
  .label__count-number { font-size: 21px; line-height: 1; }
  .label__count-unit { font-size: 9px; line-height: 1; }
  .label__type {
    position: absolute;
    right: 6px;
    bottom: 30px;
    writing-mode: vertical-rl;
    transform: rotate(180deg);
    font-family: "Arimo", sans-serif;
    font-weight: 700;
    font-size: 21px;
    line-height: 0.85;
    letter-spacing: 0.2px;
  }

  .brand {
    position: absolute;
    left: 0;
    right: 0;
    top: 1052px;
    display: flex;
    justify-content: center;
    align-items: center;
    gap: 12px;
  }
  .brand__dot {
    width: 26px;
    height: 26px;
    border-radius: 50%;
    background: var(--brand-dot);
  }
  .brand__name {
    font-family: "Nunito", sans-serif;
    font-weight: 800;
    font-size: 36px;
    color: var(--brand-ink);
    letter-spacing: 0.3px;
  }
</style>
</head>
<body>
<main class="range">

  <section class="label label--tummy">
    <svg class="label__frame" viewBox="0 0 104 104" aria-hidden="true">
      <path d="M1.5 24V1.5H24 M80 1.5H102.5V24 M1.5 80V102.5H24 M80 102.5H102.5V80" fill="none" stroke="#fff" stroke-width="2"/>
    </svg>
    <h2 class="label__name"><span>Tummy</span><span>Balance</span></h2>
    <p class="label__tagline">Oxygenating<br>Colon Cleanse*</p>
    <p class="label__count"><span class="label__count-number">90</span><span class="label__count-unit">Vegetable<br>Capsules</span></p>
    <p class="label__type">Dietary<br>Supplement</p>
  </section>

  <section class="label label--hormone">
    <svg class="label__frame" viewBox="0 0 104 104" aria-hidden="true">
      <path d="M1.5 24V1.5H24 M80 1.5H102.5V24 M1.5 80V102.5H24 M80 102.5H102.5V80" fill="none" stroke="#fff" stroke-width="2"/>
    </svg>
    <h2 class="label__name"><span>Hormone</span><span>Balance</span></h2>
    <p class="label__tagline">Supports Healthy<br>Hormone Levels*</p>
    <p class="label__count"><span class="label__count-number">60</span><span class="label__count-unit">Vegetable<br>Capsules</span></p>
    <p class="label__type">Dietary<br>Supplement</p>
  </section>

  <section class="label label--sugar">
    <svg class="label__frame" viewBox="0 0 104 104" aria-hidden="true">
      <path d="M1.5 24V1.5H24 M80 1.5H102.5V24 M1.5 80V102.5H24 M80 102.5H102.5V80" fill="none" stroke="#fff" stroke-width="2"/>
    </svg>
    <h2 class="label__name"><span>Blood</span><span>Sugar</span><span>Balance</span></h2>
    <p class="label__tagline">Supports Healthy<br>Blood Glucose Levels*</p>
    <p class="label__count"><span class="label__count-number">60</span><span class="label__count-unit">Vegetable<br>Capsules</span></p>
    <p class="label__type">Dietary<br>Supplement</p>
  </section>

  <section class="label label--liver">
    <svg class="label__frame" viewBox="0 0 104 104" aria-hidden="true">
      <path d="M1.5 24V1.5H24 M80 1.5H102.5V24 M1.5 80V102.5H24 M80 102.5H102.5V80" fill="none" stroke="#fff" stroke-width="2"/>
    </svg>
    <h2 class="label__name"><span>Liver</span><span>Balance</span></h2>
    <p class="label__tagline">Rejuvenating Cleanse<br>&amp; Detox Formula*</p>
    <p class="label__count"><span class="label__count-number">120</span><span class="label__count-unit">Vegetable<br>Capsules</span></p>
    <p class="label__type">Dietary<br>Supplement</p>
  </section>

  <footer class="brand">
    <span class="brand__dot" aria-hidden="true"></span>
    <span class="brand__name">Vital Tuned</span>
  </footer>

</main>
</body>
</html>
```